Bramblecove Suite Complementary Pass

I’d like a complimentary pass for any 30-minute Bramblecove Suite session. Choose one of the following options: Infrared Sauna with Red Light, Massage Chair Velquora Compression Therapy, or Paraffin Wax Hand Bath.

Please incorporate the logo and brand colors into your design. I’d like a square image that will be printed on square business cards (no rectangles).

Please refer to the logo and menu for more details.

Contact Information for Business Card

See discretion

```html
<!DOCTYPE html>
<html lang="en">
<head>
<meta charset="utf-8">
<title>Bramblecove Suite Complimentary Pass</title>
<link href="https://fonts.googleapis.com/css2?family=Bebas+Neue&family=Montserrat:wght@500&family=Raleway:wght@400;600&family=Satisfy&display=swap" rel="stylesheet">
<style>
  :root {
    --backdrop: #979797;
    --brand-purple: #452c88;
    --brand-coral: #f26649;
    --card-white: #ffffff;
    --body-grey: #474747;
    --rule-purple: #5b3f9e;
  }
  * { margin: 0; padding: 0; box-sizing: border-box; }
  html, body { width: 1200px; height: 1000px; overflow: hidden; }
  body { background: var(--backdrop); position: relative; }

  .card {
    position: absolute;
    top: 268px;
    width: 520px;
    height: 519px;
    border-radius: 50px;
    overflow: hidden;
  }
  .card--front { left: 70px; background: var(--brand-purple); }
  .card--back { left: 610px; background: var(--card-white); }

  .front-offer {
    position: absolute;
    left: 0; right: 0;
    top: 183px;
    text-align: center;
    color: var(--card-white);
  }
  .front-offer__lead {
    font-family: "Montserrat", sans-serif;
    font-weight: 500;
    font-size: 21px;
    line-height: 28px;
  }
  .front-offer__duration {
    font-family: "Bebas Neue", sans-serif;
    font-size: 118px;
    line-height: 96px;
    color: var(--brand-coral);
    letter-spacing: 1px;
    margin-top: 4px;
  }
  .front-offer__session {
    font-family: "Satisfy", cursive;
    font-size: 40px;
    line-height: 44px;
    margin-top: -8px;
  }

  .back-title {
    position: absolute;
    left: 45px;
    top: 68px;
  }
  .back-title__duration {
    font-family: "Bebas Neue", sans-serif;
    font-size: 68px;
    line-height: 58px;
    color: var(--brand-coral);
  }
  .back-title__session {
    font-family: "Satisfy", cursive;
    font-size: 21px;
    line-height: 22px;
    color: var(--brand-purple);
    margin-top: -6px;
  }

  .option-list {
    position: absolute;
    left: 45px;
    top: 196px;
    width: 432px;
    list-style: none;
    font-family: "Raleway", sans-serif;
    font-size: 28px;
    line-height: 36px;
    color: var(--body-grey);
  }
  .option-list__item {
    position: relative;
    padding: 0 0 7px 21px;
    border-bottom: 1px solid var(--rule-purple);
    margin-bottom: 10px;
  }
  .option-list__item:last-child { border-bottom: none; }
  .option-list__item::before {
    content: "";
    position: absolute;
    left: 0;
    top: 14px;
    width: 10px;
    height: 10px;
    border-radius: 50%;
    background: var(--brand-coral);
  }

  .brand-name {
    position: absolute;
    left: 45px;
    top: 428px;
    display: flex;
    align-items: center;
    gap: 12px;
  }
  .brand-name__mark {
    width: 22px;
    height: 22px;
    background: var(--brand-coral);
  }
  .brand-name__text {
    font-family: "Raleway", sans-serif;
    font-weight: 600;
    font-size: 38px;
    line-height: 44px;
    color: var(--brand-purple);
  }
</style>
</head>
<body>
  <section class="card card--front">
    <div class="front-offer">
      <p class="front-offer__lead">I’d like a complimentary pass for any</p>
      <p class="front-offer__duration">30-Minute</p>
      <p class="front-offer__session">Bramblecove Suite Session</p>
    </div>
  </section>

  <section class="card card--back">
    <div class="back-title">
      <p class="back-title__duration">30-Minute</p>
      <p class="back-title__session">Bramblecove Suite Session</p>
    </div>
    <ul class="option-list">
      <li class="option-list__item">Infrared Sauna with Red Light</li>
      <li class="option-list__item">Massage Chair Velquora Compression Therapy</li>
      <li class="option-list__item">Paraffin Wax Hand Bath</li>
    </ul>
    <div class="brand-name">
      <span class="brand-name__mark"></span>
      <span class="brand-name__text">solvena</span>
    </div>
  </section>
</body>
</html>
```